Package design for Terrarium Kit

We are putting together a kit to allow people to put build their own terrarium. Our company 'Brightway Goods' is using the items in a kit supplied by Fern Hollow and adding a 700ml glass jar with a cork lid and rebranding it. We will be using a similar box to the existing Fern Hollow kit and we are asking you to design a new 'wrap' for it with our logo and suggestions about a name for the product. The kit will be Australian Made.
Updates

Project Deadline Extended
Reason: We realise that to get the quality of design that we are after that you would require more time.

Target Market(s)

People wanting something on their desks, a gift for someone. We will sell it to nurseries, gift shops etc.

Industry/Entity Type

It Company

Requirements
Must have
• Front and back designs.
Nice to have
• Looking for a simple design that is self explanatory but is eye-catching.

```html
<!DOCTYPE html>
<html lang="en">
<head>
<meta charset="utf-8">
<title>DIY Terrarium Set – Box Wrap Label</title>
<link rel="stylesheet" href="https://fonts.googleapis.com/css2?family=Amatic+SC:wght@400;700&family=Tinos&display=swap">
<style>
  :root {
    --canvas-bg: #efece6;
    --ink: #111111;
    --paper: #ffffff;
    --accent-yellow: #e6e827;
    --photo-leaf: #9fb08a;
    --photo-bloom: #c9876a;
    --photo-haze: #d9ddd0;
    --photo-pebble: #f1efe9;
    --photo-soil: #2a2a2a;
  }
  * { margin: 0; padding: 0; box-sizing: border-box; }
  html, body {
    width: 1200px;
    height: 900px;
    overflow: hidden;
    background: var(--canvas-bg);
  }
  .canvas {
    position: relative;
    width: 1200px;
    height: 900px;
  }
  .wrap-label {
    position: absolute;
    left: 277px;
    top: 60px;
    width: 645px;
    height: 780px;
    box-shadow: 0 6px 24px rgba(0,0,0,0.18);
  }
  .hand-type {
    font-family: "Amatic SC", cursive;
    fill: var(--paper);
  }
  .product-title { font-size: 54px; font-weight: 700; letter-spacing: 2px; }
  .origin-line { font-size: 28px; font-weight: 700; letter-spacing: 2px; }
  .brand-name {
    font-family: "Tinos", serif;
    font-size: 40px;
    fill: var(--paper);
  }
  .contents-heading { font-size: 28px; }
  .contents-list { font-size: 28px; }
</style>
</head>
<body>
<main class="canvas">
  <svg class="wrap-label" viewBox="0 0 645 780" xmlns="http://www.w3.org/2000/svg">
    <defs>
      <linearGradient id="terrarium-photo-tone" x1="0" y1="0" x2="0" y2="1">
        <stop offset="0" stop-color="var(--photo-leaf)"/>
        <stop offset="0.18" stop-color="var(--photo-bloom)"/>
        <stop offset="0.38" stop-color="var(--photo-haze)"/>
        <stop offset="0.62" stop-color="var(--photo-haze)"/>
        <stop offset="0.72" stop-color="var(--photo-pebble)"/>
        <stop offset="0.84" stop-color="var(--photo-pebble)"/>
        <stop offset="1" stop-color="var(--photo-soil)"/>
      </linearGradient>
      <path id="title-arc" d="M 142 372 A 185 185 0 0 1 502 372"/>
    </defs>

    <rect class="label-photo" x="0" y="0" width="645" height="624" fill="url(#terrarium-photo-tone)"
          role="img" aria-label="Close-up photograph of a terrarium with plants above white pebbles and dark charcoal"/>

    <rect class="contents-band" x="0" y="624" width="645" height="156" fill="var(--ink)"/>
    <text class="hand-type contents-heading" x="22" y="672">Set contains:</text>
    <text class="hand-type contents-list" x="22" y="702">glass jar &amp; cork lid, pebbles, moss, charcoal, miniatures &amp; instructions</text>

    <g class="brand-seal">
      <ellipse cx="322" cy="330" rx="255" ry="228" fill="var(--ink)"/>
      <text class="hand-type product-title" text-anchor="middle">
        <textPath href="#title-arc" startOffset="50%">DIY TERARIUM SET</textPath>
      </text>
      <circle cx="160" cy="332" r="15" fill="var(--accent-yellow)"/>
      <text class="brand-name" x="190" y="346">Brightway Goods</text>
      <text class="hand-type origin-line" x="322" y="486" text-anchor="middle">AUSTRALIAN MADE</text>
    </g>
  </svg>
</main>
</body>
</html>
```